Brantel - Business Card Design

Design a modern masculine business card for our business

Target Market(s)

Private Market

Industry/Entity Type

Construction

Contact Information for Business Card

Company Name - Name of Person - Address - email address - contact number

Font styles to use
Serif
Sans Serif

Colors
0094D4
00A9DD
6FCCEA
C7EBF8
E9F6FB
00AB8E
00BBA5
67D7C9
C6EFE9
E9F9F6
F0912C
F2A743
F7CA91
FBE8D2
FDF5EE

Requirements
Must have
• Use company logo provided
Nice to have
• Company Logo

```html
<!DOCTYPE html>
<html lang="en">
<head>
<meta charset="utf-8">
<title>Brantel Construction – Business Card</title>
<link rel="stylesheet" href="https://fonts.googleapis.com/css2?family=Montserrat:wght@700&family=Roboto:wght@400;700&display=swap">
<style>
  :root {
    --stage: #9a9a9a;
    --paper: #f7f7f5;
    --ink: #1d1d1d;
    --grey-text: #6b6b6b;
    --orange: #ee7a2f;
    --edge: #e0611c;
    --black-card: #121212;
    --white: #f4f4f4;
  }
  * { box-sizing: border-box; margin: 0; padding: 0; }
  html, body { width: 1200px; height: 1153px; overflow: hidden; }
  body {
    background: var(--stage);
    font-family: "Roboto", Arial, sans-serif;
    position: relative;
  }
  .card {
    position: absolute;
    left: 280px;
    width: 640px;
    height: 366px;
    border-bottom: 4px solid var(--edge);
    box-shadow: 0 18px 40px rgba(0,0,0,.28);
  }
  .card--front { top: 176px; background: var(--paper); }
  .card--back { top: 610px; background: var(--black-card); display: flex; align-items: center; justify-content: center; }

  .wordmark { display: flex; align-items: center; gap: 12px; font-family: "Roboto", Arial, sans-serif; font-weight: 700; line-height: 1; white-space: nowrap; }
  .wordmark__mark { width: 24px; height: 24px; background: var(--orange); flex: none; }
  .card--front .wordmark { position: absolute; right: 48px; top: 64px; color: var(--ink); font-size: 52px; }
  .card--back .wordmark { color: var(--white); font-size: 72px; gap: 18px; }
  .card--back .wordmark__mark { width: 36px; height: 36px; }

  .person { position: absolute; left: 48px; top: 150px; }
  .person__name { font-family: "Montserrat", Arial, sans-serif; font-weight: 700; font-size: 19px; line-height: 24px; color: var(--ink); letter-spacing: .3px; }
  .person__title { font-size: 17px; line-height: 22px; color: var(--orange); }

  .rule { position: absolute; left: 180px; right: 48px; top: 188px; height: 1.5px; background: var(--orange); }

  .contact { position: absolute; left: 48px; top: 218px; list-style: none; }
  .contact li { display: flex; align-items: center; gap: 10px; font-size: 16px; color: var(--grey-text); height: 26px; }
  .contact svg { width: 18px; height: 18px; flex: none; }

  .address { position: absolute; right: 48px; bottom: 44px; text-align right; text-align: right; font-size: 16px; line-height: 1.35; color: var(--grey-text); font-style: normal; }
</style>
</head>
<body>
  <section class="card card--front">
    <div class="wordmark"><span class="wordmark__mark"></span><span class="wordmark__name">BRANTEL</span></div>

    <div class="person">
      <h1 class="person__name">DALEN R. MARSH</h1>
      <p class="person__title">Founder &amp; CEO</p>
    </div>
    <div class="rule"></div>

    <ul class="contact">
      <li>
        <svg viewBox="0 0 20 20"><circle cx="10" cy="10" r="10" fill="var(--orange)"/><path d="M7 5.5l1.6 2.3-1 1.1a6 6 0 0 0 3.5 3.5l1.1-1 2.3 1.6-.9 1.6c-3.8-.4-7.1-3.7-7.5-7.5z" fill="#fff"/></svg>
        (555)014-2870
      </li>
      <li>
        <svg viewBox="0 0 20 20"><circle cx="10" cy="10" r="10" fill="var(--orange)"/><rect x="5" y="6.5" width="10" height="7" fill="none" stroke="#fff" stroke-width="1.2"/><path d="M5 6.5l5 4 5-4" fill="none" stroke="#fff" stroke-width="1.2"/></svg>
        info@brantelbuild.com
      </li>
      <li>
        <svg viewBox="0 0 20 20"><circle cx="10" cy="10" r="10" fill="var(--orange)"/><circle cx="10" cy="10" r="5" fill="none" stroke="#fff" stroke-width="1.1"/><ellipse cx="10" cy="10" rx="2.2" ry="5" fill="none" stroke="#fff" stroke-width="1"/><path d="M5 10h10" stroke="#fff" stroke-width="1"/></svg>
        www.brantelbuild.com
      </li>
    </ul>

    <address class="address">
      Brantel Construction, Inc<br>
      4820 Harbor Crest Drive<br>
      Calder, CA 90000
    </address>
  </section>

  <section class="card card--back">
    <div class="wordmark"><span class="wordmark__mark"></span><span class="wordmark__name">BRANTEL</span></div>
  </section>
</body>
</html>
```